Need to create a website for a luxury custom home builder in Phoenix USA. Looking forward for some creative designs including a full page video intro on homepage and should show up pretty luxurious.

```html
<!DOCTYPE html>
<html lang="en">
<head>
<meta charset="utf-8">
<title>Crestline Homes — Luxury Custom Home Builder</title>
<link rel="stylesheet" href="https://fonts.googleapis.com/css2?family=Rubik:wght@500;600&family=Poppins:wght@400;500;600&family=Barlow+Condensed:wght@600&display=swap">
<style>
:root{
  --blue:#1b8fd5;
  --blue-dark:#1677b8;
  --teal:#19a486;
  --teal-dark:#14907a;
  --ink:#1d1d1f;
  --text:#4a4f55;
  --muted:#6b7178;
  --white:#ffffff;
  --svc-bg:#e3eff7;
  --line:#c9d3da;
}
*{margin:0;padding:0;box-sizing:border-box}
html,body{width:1200px;height:3637px;overflow:hidden}
body{position:relative;background:var(--white);font-family:"Poppins",sans-serif;color:var(--text)}
.abs{position:absolute}
.heading{font-family:"Rubik",sans-serif;font-weight:600;color:var(--ink)}
.btn{position:absolute;display:flex;align-items:center;justify-content:center;gap:10px;color:var(--white);font-family:"Poppins",sans-serif;font-weight:600;font-size:14px;text-transform:uppercase;border-radius:3px;letter-spacing:.2px;text-decoration:none}
.btn svg{width:8px;height:10px}
.btn--teal{background:var(--teal)}
.btn--blue{background:var(--blue)}
.rule{position:absolute;height:10px}
.rule i{position:absolute;left:0;top:0;width:10px;height:10px;background:var(--blue)}
.rule b{position:absolute;left:0;right:0;top:4px;height:1.5px;background:var(--blue)}
.rule--light i,.rule--light b{background:var(--white)}

/* header */
.site-header{left:0;top:0;width:1200px;height:76px;background:var(--white)}
.brand{display:flex;align-items:center;gap:10px}
.brand__dot{width:36px;height:36px;border-radius:50%;background:var(--blue)}
.brand__name{font-family:"Rubik",sans-serif;font-weight:600;font-size:27px;color:var(--blue);letter-spacing:.5px;white-space:nowrap}
.main-nav a{position:absolute;top:35px;font-size:14px;font-weight:500;color:var(--ink);text-decoration:none}
.main-nav a.is-active{color:var(--blue)}

/* hero */
.hero{left:0;top:76px;width:1200px;height:740px}
.hero__title{left:107px;top:268px;font-size:68px;color:var(--white);letter-spacing:-.5px;white-space:nowrap}
.hero__lead{left:112px;top:364px;width:560px;font-size:21px;font-weight:500;line-height:33px;color:var(--white)}
.hero__play{left:112px;top:522px;display:flex;align-items:center;gap:12px;color:var(--white);font-size:16px}
.hero__play span{text-decoration:underline;text-underline-offset:4px}
.play-icon{width:42px;height:42px;border-radius:50%;background:var(--white);display:flex;align-items:center;justify-content:center}

/* about */
.about__body{position:absolute;left:606px;top:888px;width:474px}
.about__title{font-size:42px;line-height:50px}
.about__rule{position:relative;width:126px;margin:10px 0 14px}
.about__body p{font-size:14px;line-height:24.8px;color:var(--text);text-align:justify}
.about__body p + p{margin-top:8px}
.about__body .btn{position:relative;width:146px;height:46px;margin-top:19px}

/* services */
.services{left:0;top:1381px;width:1200px;height:716px;background:linear-gradient(180deg,#e9f3fa 0%,#dfeef7 100%)}
.section-title{position:absolute;left:0;width:1200px;text-align:center;font-size:42px}
.svc-box{position:absolute;width:69px;height:69px;background:var(--white);border:1.5px solid #9aa4ab;border-radius:6px;display:flex;align-items:center;justify-content:center}
.svc-box svg{width:40px;height:40px;fill:none;stroke:var(--ink);stroke-width:1.6;stroke-linecap:round;stroke-linejoin:round}
.svc{position:absolute;width:270px}
.svc h3{font-family:"Rubik",sans-serif;font-weight:500;font-size:20px;line-height:21px;color:var(--ink);margin-bottom:8px}
.svc p{font-size:13px;line-height:21.5px;color:var(--muted)}
.svc--left{text-align:right}

/* gallery */
.gallery{left:0;top:2097px;width:1200px;height:826px;background:var(--teal)}
.gallery .section-title{color:var(--white)}
.photo{position:absolute}

/* newsletter */
.newsletter__text{left:200px;top:3073px;width:800px;text-align:center;font-size:15px;line-height:24.5px}
.field{position:absolute;top:3146px;height:42px;background:var(--blue);border:1px solid var(--blue-dark);border-radius:2px;color:#e6f3fc;font-size:13px;padding-left:18px;display:flex;align-items:center}

/* footer */
.site-footer{left:0;top:3242px;width:1200px;height:395px;background:linear-gradient(180deg,#ffffff 0%,#f1f4f6 100%)}
.divider{position:absolute;left:111px;width:977px;height:1px;background:var(--line)}
.foot-col{position:absolute;top:3284px}
.foot-col h4{font-family:"Barlow Condensed",sans-serif;font-weight:600;font-size:25px;color:#2b2f33;letter-spacing:.3px}
.foot-col hr{border:0;height:2px;width:50px;background:var(--blue);margin:6px 0 14px}
.foot-col li{list-style:none;font-size:13px;line-height:26.6px;color:#2b2f33;text-transform:uppercase}
.social{position:absolute;top:3460px;width:28px;height:28px;border-radius:50%;background:var(--blue)}
.copyright{left:0;top:3578px;width:1200px;text-align:center;font-size:14px;color:#2b2f33}
.to-top{left:1141px;top:3534px;width:40px;height:40px;border-radius:7px;background:var(--blue);display:flex;align-items:center;justify-content:center}
</style>
</head>
<body>

<header class="site-header abs">
  <div class="brand abs" style="left:112px;top:18px">
    <div class="brand__dot"></div>
    <div class="brand__name">CRESTLINE HOMES</div>
  </div>
  <nav class="main-nav">
    <a class="is-active" style="left:513px">HOME</a>
    <a style="left:587px">ABOUT</a>
    <a style="left:667px">TESTIMONIALS</a>
    <a style="left:796px">FAQ</a>
    <a style="left:858px">SERVICES</a>
  </nav>
  <a class="btn btn--teal" style="left:942px;top:21px;width:146px;height:46px">Contact Us
    <svg viewBox="0 0 8 10"><path d="M2 1l4 4-4 4" fill="none" stroke="#fff" stroke-width="1.6"/></svg></a>
</header>

<section class="hero abs">
  <svg width="1200" height="740" viewBox="0 0 1200 740" style="position:absolute;left:0;top:0">
    <defs>
      <linearGradient id="heroTone" x1="0" y1="0" x2="1" y2="1">
        <stop offset="0" stop-color="#3b3f4a"/>
        <stop offset=".45" stop-color="#5a4a4a"/>
        <stop offset=".75" stop-color="#2c2f38"/>
        <stop offset="1" stop-color="#1f2128"/>
      </linearGradient>
    </defs>
    <polygon role="img" aria-label="Evening view of a luxury home patio with lounge seating and fireplace" points="0,0 1200,0 1200,580 595,720 0,580" fill="url(#heroTone)"/>
    <polygon points="240,645 595,736 960,645 595,724" fill="var(--blue)"/>
    <circle cx="568" cy="678" r="5" fill="none" stroke="#fff" stroke-width="1.5"/>
    <circle cx="589" cy="678" r="6" fill="var(--blue)"/>
    <circle cx="610" cy="678" r="5" fill="none" stroke="#fff" stroke-width="1.5"/>
    <circle cx="631" cy="678" r="5" fill="none" stroke="#fff" stroke-width="1.5"/>
  </svg>
</section>
<h1 class="heading hero__title abs">Crestline Homes</h1>
<p class="hero__lead abs">Saers Ikses sepiciatisunde omnisiste natuserror sivoluptatem asccusan tium doloremque.</p>
<a class="btn btn--teal" style="left:112px;top:459px;width:146px;height:45px">Get Started
  <svg viewBox="0 0 8 10"><path d="M2 1l4 4-4 4" fill="none" stroke="#fff" stroke-width="1.6"/></svg></a>
<div class="hero__play abs">
  <div class="play-icon"><svg width="14" height="16" viewBox="0 0 14 16"><path d="M2 1l11 7-11 7z" fill="var(--blue-dark)"/></svg></div>
  <span>Play Video</span>
</div>

<section class="about">
  <svg class="abs" style="left:150px;top:908px" width="380" height="330" viewBox="0 0 380 330">
    <circle cx="180" cy="150" r="125" fill="var(--blue)" opacity=".85"/>
  </svg>
  <div class="about__body">
    <h2 class="heading about__title">About Us</h2>
    <div class="rule about__rule"><b></b><i></i></div>
    <p>Saerspiciatis undeasepoiise oklasdo mnis aidaste natus error sit voluptatem accusan tium doloremque laudantium, totam rem aperiam, ease aque ipaefdsa quae ab illo inventore veritatis ease quasi architecto beatae vitae dicta sunt explicabo. Nemo enim ipsam voluptatem quia volasdfupta sde sessitasese aspernatur autodit aut fugitsdsed quisaea consequuntur magni dolores eos qui ratione voluptatem sequi nesciunt.</p>
    <p>Dseste natus error sit voluptatem accusan tium doloremque laudantium, totam rem aperiam, ease aque ipaefdsa quae ab illo inventore veritatis ease quasi architecto.</p>
    <a class="btn btn--teal">Learn More
      <svg viewBox="0 0 8 10"><path d="M2 1l4 4-4 4" fill="none" stroke="#fff" stroke-width="1.6"/></svg></a>
  </div>
</section>

<section class="services abs">
  <h2 class="heading section-title" style="top:70px">Our Services</h2>
  <div class="rule" style="left:470px;top:128px;width:130px"><b></b><i></i></div>
  <svg class="abs" style="left:0;top:0" width="1200" height="716" viewBox="0 0 1200 716">
    <path d="M420 234 Q330 394 420 554" fill="none" stroke="#9aa4ab" stroke-width="1.5"/>
    <path d="M780 234 Q870 394 780 554" fill="none" stroke="#9aa4ab" stroke-width="1.5"/>
    <circle cx="594" cy="394" r="162" fill="#fff" stroke="var(--blue)" stroke-width="2"/>
    <circle role="img" aria-label="Modern white two-storey villa beside a swimming pool" cx="594" cy="394" r="146" fill="#b9cfdc"/>
  </svg>
  <div class="svc svc--left" style="left:111px;top:185px"><h3>Green Building and<br>Sustainability</h3><p>Werspiciatis asesertu undeas eomnis iste natus error asese sitvolasuptate masease accusantium emiumtotam.</p></div>
  <div class="svc svc--left" style="left:52px;top:354px"><h3>Home<br>Additions</h3><p>Werspiciatis asesertu undeas eomnis iste natus error asese sitvolasuptate masease accusantium emiumtotam.</p></div>
  <div class="svc svc--left" style="left:111px;top:522px"><h3>Design-Build<br>Services</h3><p>Werspiciatis asesertu undeas eomnis iste natus error asese sitvolasuptate masease accusantium emiumtotam.</p></div>
  <div class="svc" style="left:819px;top:185px"><h3>Custom Home<br>Construction</h3><p>Werspiciatis asesertu undeas eomnis iste natus error asese sitvolasuptate masease accusantium emiumtotam.</p></div>
  <div class="svc" style="left:871px;top:354px"><h3>Spec Home<br>Construction</h3><p>Werspiciatis asesertu undeas eomnis iste natus error asese sitvolasuptate masease accusantium emiumtotam.</p></div>
  <div class="svc" style="left:819px;top:522px"><h3>Renovations and<br>Remodeling</h3><p>Werspiciatis asesertu undeas eomnis iste natus error asese sitvolasuptate masease accusantium emiumtotam.</p></div>

  <div class="svc-box" style="left:390px;top:199px"><svg viewBox="0 0 40 40"><rect x="5" y="14" width="30" height="20"/><path d="M5 21h30M5 28h30M14 14v7M26 14v7M20 21v7M14 28v6M26 28v6"/></svg></div>
  <div class="svc-box" style="left:336px;top:368px"><svg viewBox="0 0 40 40"><path d="M12 36V6M8 36h8M12 8h22M12 14l10-6M30 8v10M27 18h6v5h-6z"/></svg></div>
  <div class="svc-box" style="left:390px;top:536px"><svg viewBox="0 0 40 40"><path d="M6 36l2-9 8-3h8l8 3 2 9M14 16a6 6 0 0 0 12 0M12 16h16M14 16a6 6 0 0 1 12 0"/></svg></div>
  <div class="svc-box" style="left:741px;top:199px"><svg viewBox="0 0 40 40"><path d="M8 34V12M8 12l4 4M8 12l-4 4M20 34V8M32 34V16M4 34h32"/><circle cx="32" cy="12" r="4"/></svg></div>
  <div class="svc-box" style="left:793px;top:368px"><svg viewBox="0 0 40 40"><path d="M10 6h18l4 4v24H10z M14 14h14M14 20h14M14 26h10"/></svg></div>
  <div class="svc-box" style="left:741px;top:536px"><svg viewBox="0 0 40 40"><rect x="5" y="10" width="30" height="24"/><path d="M10 28l6-8 6 5 8-10"/></svg></div>
</section>

<section class="gallery abs">
  <h2 class="heading section-title" style="top:72px">Gallery</h2>
  <div class="rule rule--light" style="left:527px;top:128px;width:127px"><b></b><i></i></div>
  <div class="photo" role="img" aria-label="Pool terrace of a white colonial-style house" style="left:109px;top:159px;width:237px;height:246px;background:linear-gradient(160deg,#d7e6ee,#5bb7d6)"></div>
  <div class="photo" role="img" aria-label="Modern white villa with a pool under misty hills" style="left:359px;top:159px;width:480px;height:246px;background:linear-gradient(180deg,#8b9392,#c9ccc7 55%,#3b5357)"></div>
  <div class="photo" role="img" aria-label="Two-storey grey suburban house with garage" style="left:851px;top:159px;width:237px;height:246px;background:linear-gradient(180deg,#c9d4df,#4d5158)"></div>
  <div class="photo" role="img" aria-label="Contemporary white house reflected in a pool" style="left:109px;top:417px;width:484px;height:246px;background:linear-gradient(180deg,#b5c2c6,#e2e4e1 50%,#263b47)"></div>
  <div class="photo" role="img" aria-label="Glass pavilion house lit at dusk beside a pool" style="left:604px;top:417px;width:486px;height:246px;background:linear-gradient(180deg,#2f3b39,#6a5542 55%,#1d4a4c)"></div>
  <a class="btn btn--blue" style="left:527px;top:691px;width:146px;height:47px">View More
    <svg viewBox="0 0 8 10"><path d="M2 1l4 4-4 4" fill="none" stroke="#fff" stroke-width="1.6"/></svg></a>
</section>

<section class="newsletter">
  <h2 class="heading section-title" style="top:2990px">Sign Up For Our Newsletter</h2>
  <div class="rule" style="left:328px;top:3050px;width:127px"><b></b><i></i></div>
  <p class="newsletter__text abs">Saerspiciatis undeasepoiise oklasdo mnis aidaste natus error sit voluptatem accusan tium doloremque laudantium, totam rem aperiam, ease aque ipaefdsa.</p>
  <div class="field" style="left:225px;width:287px">Your Name</div>
  <div class="field" style="left:529px;width:287px">Email</div>
  <a class="btn btn--teal" style="left:827px;top:3146px;width:147px;height:45px">Learn More
    <svg viewBox="0 0 8 10"><path d="M2 1l4 4-4 4" fill="none" stroke="#fff" stroke-width="1.6"/></svg></a>
</section>

<footer class="site-footer abs"></footer>
<div class="divider" style="top:3242px"></div>
<div class="brand abs" style="left:150px;top:3378px">
  <div class="brand__dot" style="width:40px;height:40px"></div>
  <div class="brand__name" style="font-size:30px">CRESTLINE HOMES</div>
</div>
<span class="social" style="left:304px"></span>
<span class="social" style="left:346px"></span>
<div class="foot-col" style="left:548px"><h4>QUICK LINKS</h4><hr><ul><li>Home</li><li>About</li><li>Testimonials</li><li>FAQ</li><li>Services</li><li>Contact Us</li></ul></div>
<div class="foot-col" style="left:784px"><h4>LINKS</h4><hr><ul><li>Copyright</li><li>Legal</li><li>Privacy</li><li>Accessibility</li><li>Sitemap</li></ul></div>
<div class="foot-col" style="left:963px"><h4>SUPPORT</h4><hr><ul><li>Team</li><li>About Us</li><li>Careers</li><li>Our Values</li></ul></div>
<div class="divider" style="top:3551px"></div>
<p class="copyright abs">©2023. All rights reserved.</p>
<div class="to-top abs"><svg width="12" height="8" viewBox="0 0 12 8"><path d="M1 7l5-5 5 5" fill="none" stroke="#fff" stroke-width="1.8"/></svg></div>

</body>
</html>
```